Banner Ad Design for Resume Builder Needed

For the ad copy and design of the ad, I leave that up to you. Keep in mind this is a do-it-yourself online resume builder. The site is simple to use and geared towards people who are unsure of how to write/create their own resume.

You can view the site (which isn't finished) and how it works at http://careerforge.demo.tlvworks.net/

I do not want the same color scheme or the logo used in the ad, just the most appealing ad for those looking to use a product like this

I need the ad in these sizes:

300x250, 728x90, 160x600, 468x60, 120x600, 300x100

```html
<!DOCTYPE html>
<html lang="en">
<head>
<meta charset="utf-8">
<title>Resume Builder Banner Set</title>
<link rel="stylesheet" href="https://fonts.googleapis.com/css2?family=Source+Sans+3:wght@400;600;700;800&display=swap">
<style>
:root{
  --navy:#173a5e;
  --navy-deep:#12304f;
  --blue:#1d5a86;
  --teal:#1f6690;
  --orange:#f07f23;
  --orange-deep:#e2711a;
  --cream:#f4efe6;
  --ink:#1b2b3c;
  --white:#ffffff;
  --green:#23962f;
  --green-dark:#0c5316;
  --yellow:#f3f03c;
  --stage:#b4b2ae;
  --stage-edge:#6f6e6b;
  --font:"Source Sans 3", "Myriad Pro", Arial, sans-serif;
}
*{box-sizing:border-box;margin:0;padding:0}
html,body{width:1200px;height:1000px;overflow:hidden}
body{
  position:relative;
  font-family:var(--font);
  background:radial-gradient(ellipse at 50% 45%, var(--stage) 62%, var(--stage-edge) 100%);
}
.banner{position:absolute;overflow:hidden;border:1px solid #8a6a4c;box-shadow:0 0 2px rgba(0,0,0,.25)}
.cell{position:absolute;display:flex;flex-direction:column;align-items:center;justify-content:center;text-align:center}
.navy{background:var(--navy)}
.orange{background:var(--orange)}
.orange-deep{background:var(--orange-deep)}
.blue{background:var(--blue)}
.teal{background:var(--teal)}
.logo{font-weight:800;color:var(--orange);line-height:1;letter-spacing:.5px}
.pitch{color:var(--white);font-weight:400;line-height:1.2}
.pitch .hl{color:var(--orange)}
.pitch .you{color:var(--orange);font-weight:700}
.feature{color:var(--navy);font-weight:700;line-height:1.15}
.feature-light{color:var(--orange);font-weight:700;line-height:1.2}
.icon{fill:none;stroke:var(--navy);stroke-width:5}
.icon-fill{fill:var(--navy)}
.cta{
  display:flex;flex-direction:column;align-items:center;justify-content:center;
  border-radius:10px;
  background:radial-gradient(ellipse at 50% 40%, var(--green) 40%, var(--green-dark) 100%);
  box-shadow:0 3px 6px rgba(0,0,0,.55), inset 0 0 6px rgba(0,0,0,.3);
  font-weight:700;line-height:1.05;text-align:center;
}
.cta .try{color:var(--white)}
.cta .click{color:var(--yellow)}
.cta.row{flex-direction:row;gap:22px}
.art-paper{background:linear-gradient(160deg,var(--cream),#ddd6ca)}
.feature-row{position:absolute;display:flex;align-items:center}
</style>
</head>
<body>

<svg width="0" height="0" style="position:absolute">
  <defs>
    <symbol id="i-clock" viewBox="0 0 60 60">
      <circle cx="30" cy="30" r="25" fill="none" stroke="currentColor" stroke-width="5"/>
      <g stroke="currentColor" stroke-width="3" stroke-linecap="round">
        <line x1="30" y1="9" x2="30" y2="13"/><line x1="30" y1="47" x2="30" y2="51"/>
        <line x1="9" y1="30" x2="13" y2="30"/><line x1="47" y1="30" x2="51" y2="30"/>
      </g>
      <g stroke="currentColor" stroke-width="4" stroke-linecap="round">
        <line x1="30" y1="30" x2="30" y2="16"/><line x1="30" y1="30" x2="40" y2="37"/>
      </g>
    </symbol>
    <symbol id="i-ring" viewBox="0 0 60 60">
      <circle cx="30" cy="30" r="24" fill="none" stroke="currentColor" stroke-width="6"/>
      <circle cx="30" cy="30" r="12" fill="none" stroke="currentColor" stroke-width="5"/>
      <g stroke="currentColor" stroke-width="9">
        <line x1="13" y1="13" x2="21" y2="21"/><line x1="47" y1="13" x2="39" y2="21"/>
        <line x1="13" y1="47" x2="21" y2="39"/><line x1="47" y1="47" x2="39" y2="39"/>
      </g>
    </symbol>
    <symbol id="i-cap" viewBox="0 0 70 50">
      <polygon points="35,4 68,18 35,32 2,18" fill="currentColor"/>
      <path d="M15 24 V38 Q35 48 55 38 V24 L35 33 Z" fill="currentColor"/>
      <line x1="62" y1="20" x2="62" y2="36" stroke="currentColor" stroke-width="2.5"/>
    </symbol>
  </defs>
</svg>

<!-- Skyscraper 120x600 -->
<section class="banner" style="left:78px;top:24px;width:141px;height:702px" aria-label="Skyscraper banner">
  <div class="cell navy" style="left:0;top:0;width:141px;height:132px">
    <div class="logo" style="font-size:40px">LOGO</div>
    <div class="pitch" style="font-size:17px;margin-top:6px">Build a <span class="hl">Resume</span><br>personalized to<br><span class="you">YOU</span></div>
  </div>
  <div class="art-paper" role="img" aria-label="Sample resume page with name heading and text lines" style="position:absolute;left:0;top:132px;width:141px;height:160px"></div>
  <div class="feature-row orange" style="left:0;top:292px;width:141px;height:62px;padding:0 4px">
    <svg width="48" height="48" style="color:var(--navy);flex:none"><use href="#i-clock"/></svg>
    <div class="feature" style="font-size:13px;flex:1;text-align:center">Professional resume in minutes</div>
  </div>
  <div class="feature-row orange-deep" style="left:0;top:354px;width:141px;height:62px;padding:0 4px">
    <svg width="48" height="48" style="color:var(--navy);flex:none"><use href="#i-ring"/></svg>
    <div class="feature" style="font-size:13px;flex:1;text-align:center">Ask career counselors questions</div>
  </div>
  <div class="cell orange" style="left:0;top:416px;width:141px;height:106px;padding:6px 4px;align-items:flex-end">
    <div class="feature" style="font-size:13px;text-align:right;position:relative">
      <svg width="56" height="40" style="color:var(--navy);float:left;margin:0 2px 0 0"><use href="#i-cap"/></svg>
      Insert pre written examples written by resume writing experts
    </div>
  </div>
  <div class="cell navy" style="left:0;top:522px;width:141px;height:180px">
    <div class="cta" style="width:122px;height:150px;font-size:34px"><span class="try" style="font-size:30px">Try It</span><span class="click">Click</span><span class="click">Here</span></div>
  </div>
</section>

<!-- Leaderboard 728x90 -->
<section class="banner" style="left:235px;top:24px;width:852px;height:106px" aria-label="Leaderboard banner">
  <div class="cell navy" style="left:0;top:0;width:255px;height:106px;align-items:flex-start;padding-left:12px">
    <div class="logo" style="font-size:38px;margin-left:26px">LOGO</div>
    <div class="pitch" style="font-size:16px;margin-top:4px;width:150px">Build a <span class="hl">Resume</span><br>personalized to <span class="you">YOU</span></div>
  </div>
  <div class="art-paper" role="img" aria-label="Stack of sample resume pages" style="position:absolute;left:163px;top:6px;width:88px;height:92px"></div>
  <div class="cell orange" style="left:255px;top:0;width:140px;height:106px">
    <svg width="56" height="56" style="color:var(--navy)"><use href="#i-clock"/></svg>
    <div class="feature" style="font-size:12px;margin-top:2px">Professional resume<br>in minutes</div>
  </div>
  <div class="cell orange-deep" style="left:395px;top:0;width:142px;height:106px">
    <svg width="56" height="56" style="color:var(--navy)"><use href="#i-ring"/></svg>
    <div class="feature" style="font-size:12px;margin-top:2px">Ask career counselors<br>questions</div>
  </div>
  <div class="cell orange" style="left:537px;top:0;width:156px;height:106px">
    <svg width="56" height="40" style="color:var(--navy)"><use href="#i-cap"/></svg>
    <div class="feature" style="font-size:12px;margin-top:4px">Insert pre written<br>examples written by<br>resume writing experts</div>
  </div>
  <div class="cell navy" style="left:693px;top:0;width:159px;height:106px">
    <div class="cta" style="width:138px;height:88px;font-size:26px"><span class="try">Try It</span><span class="click">Click Here</span></div>
  </div>
</section>

<!-- Medium rectangle 300x250 -->
<section class="banner" style="left:235px;top:146px;width:352px;height:293px" aria-label="Medium rectangle banner">
  <div class="cell navy" style="left:0;top:0;width:169px;height:126px">
    <div class="pitch" style="font-size:21px">Build a<br><span class="hl">Resume</span><br>personalized to<br><span class="you" style="font-weight:400">YOU</span></div>
  </div>
  <div class="cell teal" style="left:169px;top:0;width:183px;height:126px">
    <svg width="84" height="60" style="color:var(--orange)"><use href="#i-cap"/></svg>
    <div class="feature-light" style="font-size:12px;margin-top:4px">Insert pre written examples<br>written by resume<br>writing experts</div>
  </div>
  <div class="cell blue" style="left:0;top:126px;width:169px;height:103px">
    <svg width="58" height="58" style="color:var(--orange)"><use href="#i-clock"/></svg>
    <div class="feature-light" style="font-size:12px;margin-top:4px">Professional resume<br>in minutes</div>
  </div>
  <div class="cell teal" style="left:169px;top:126px;width:183px;height:103px">
    <svg width="58" height="58" style="color:var(--orange)"><use href="#i-ring"/></svg>
    <div class="feature-light" style="font-size:12px;margin-top:4px">Ask career counselors<br>questions</div>
  </div>
  <div class="feature-row orange" style="left:0;top:229px;width:352px;height:64px;padding:0 10px;gap:10px">
    <div class="logo" style="font-size:32px;color:var(--navy)">LOGO</div>
    <div class="cta row" style="width:230px;height:48px;border-radius:24px;gap:10px"><span class="try" style="font-size:18px;line-height:.9">Try<br>It</span><span class="click" style="font-size:30px">Click Here</span></div>
  </div>
</section>

<!-- Mobile banner 300x100 -->
<section class="banner" style="left:736px;top:146px;width:351px;height:117px" aria-label="Small rectangle banner">
  <div class="cell navy" style="left:0;top:0;width:132px;height:117px">
    <div class="logo" style="font-size:34px">LOGO</div>
    <div class="pitch" style="font-size:16px;margin-top:2px">Build a <span class="hl">Resume</span><br>personalized to<br><span class="you">YOU</span></div>
  </div>
  <div class="cell orange" style="left:132px;top:0;width:90px;height:117px">
    <svg width="50" height="50" style="color:var(--navy)"><use href="#i-clock"/></svg>
    <div class="feature" style="font-size:12px;margin-top:2px">Professional<br>resume in<br>minutes</div>
  </div>
  <div class="cell navy" style="left:222px;top:0;width:129px;height:117px">
    <div class="cta" style="width:106px;height:100px;font-size:25px"><span class="try">Try It</span><span class="click">Click</span><span class="click">Here</span></div>
  </div>
</section>

<!-- Full banner 468x60 -->
<section class="banner" style="left:235px;top:457px;width:548px;height:70px" aria-label="Full banner">
  <div class="cell orange" style="left:0;top:0;width:235px;height:70px">
    <div class="pitch" style="font-size:21px">Build a <span style="color:var(--navy)">Resume</span><br>personalized to <span style="color:var(--navy);font-weight:700">YOU</span></div>
  </div>
  <div class="cell navy" style="left:235px;top:0;width:313px;height:70px">
    <div class="cta row" style="width:292px;height:52px;border-radius:26px;font-size:30px"><span class="try">Try It</span><span class="click">Click Here</span></div>
  </div>
</section>

<!-- Wide skyscraper 160x600 -->
<section class="banner" style="left:900px;top:282px;width:188px;height:702px" aria-label="Wide skyscraper banner">
  <div class="cell navy" style="left:0;top:0;width:188px;height:138px">
    <div class="logo" style="font-size:42px">LOGO</div>
    <div class="pitch" style="font-size:22px;margin-top:4px">Build a <span class="hl">Resume</span><br>personalized to<br><span class="you" style="font-weight:400">YOU</span></div>
  </div>
  <div class="navy" style="position:absolute;left:0;top:138px;width:188px;height:152px"></div>
  <div class="art-paper" role="img" aria-label="Stack of sample resume pages" style="position:absolute;left:4px;top:142px;width:180px;height:126px"></div>
  <div class="feature-row orange" style="left:0;top:290px;width:188px;height:83px;padding:0 4px">
    <svg width="68" height="68" style="color:var(--navy);flex:none"><use href="#i-clock"/></svg>
    <div class="feature" style="font-size:17px;flex:1;text-align:center">Professional resume in minutes</div>
  </div>
  <div class="feature-row orange-deep" style="left:0;top:373px;width:188px;height:87px;padding:0 4px">
    <svg width="68" height="68" style="color:var(--navy);flex:none"><use href="#i-ring"/></svg>
    <div class="feature" style="font-size:17px;flex:1;text-align:center">Ask career counselors questions</div>
  </div>
  <div class="cell orange" style="left:0;top:460px;width:188px;height:134px;padding:6px;align-items:flex-end">
    <div class="feature" style="font-size:17px;text-align:right">
      <svg width="76" height="54" style="color:var(--navy);float:left;margin-right:2px"><use href="#i-cap"/></svg>
      Insert pre written examples written by resume writing experts
    </div>
  </div>
  <div class="cell navy" style="left:0;top:594px;width:188px;height:108px">
    <div class="cta" style="width:170px;height:92px;font-size:30px"><span class="try">Try It</span><span class="click">Click Here</span></div>
  </div>
</section>

</body>
</html>
```